Velvet Veil Expert 5 page Website

Modern 5 page website including: home page, Bridal Experts, services, gallery, and book me. Home page to include photo slideshow and contact information for stylist. The Bridal a Experts section will include short biography and photos of each bridal expert 3-4. Services page will include list and description of services and pricing. Gallery will contain work divided in the hair and makeup category. The book me page will contain an active booking tab with drop down service and customer information.

Target Market(s)

Brides, ages 21 to 45

Industry/Entity Type

Hair And Beauty

Coding

Coded - Design and coding required

Number of Pages Required

5+ page

Font styles to use
Serif
Decorative
Script

Colors
faa54b
97b8d9

Requirements
Must have
• Photo slideshow, photo gallery
Nice to have
• Scrolling slide show on home page

```html
<!DOCTYPE html>
<html lang="en">
<head>
<meta charset="utf-8">
<title>Velvet Veil</title>
<link rel="stylesheet" href="https://fonts.googleapis.com/css2?family=Great+Vibes&family=Open+Sans:ital,wght@0,400;0,600;0,700;1,400&display=swap">
<style>
:root{
  --orange:#e98b2a;
  --orange-light:#faa54b;
  --blue:#97b8d9;
  --dark:#3f3c3a;
  --ink:#2b2623;
  --text:#6f6a66;
  --white:#ffffff;
  --rule:#e6e2de;
}
*{margin:0;padding:0;box-sizing:border-box}
html,body{width:1200px;height:2317px;overflow:hidden;background:var(--white)}
body{position:relative;font-family:"Open Sans",Arial,sans-serif;color:var(--text)}
.abs{position:absolute}
.script{font-family:"Great Vibes",cursive;font-weight:400}

/* navigation */
.site-nav{left:0;top:0;width:1200px;height:103px;border-bottom:3px solid var(--orange)}
.nav-link{top:0;height:103px;line-height:130px;font-size:21px;color:var(--ink);text-decoration:none;transform:translateX(-50%);white-space:nowrap}
.nav-active{left:99px;top:0;width:94px;height:103px;background:var(--orange)}
.nav-link.is-active{color:var(--white)}
.brand-plate{left:484px;top:0;width:232px;height:162px;border-radius:50%;background:var(--white);z-index:3;border-bottom:3px solid var(--orange)}
.brand-name{left:484px;top:46px;width:232px;text-align:center;font-size:34px;color:var(--blue);z-index:4}

/* hero */
.photo{display:block}
.hero-main{left:0;top:103px;width:618px;height:504px;background:linear-gradient(135deg,#2f5a6a 0%,#3a4a55 45%,#6b4a3e 80%,#8a6a52 100%)}
.hero-top{left:620px;top:103px;width:580px;height:283px;background:linear-gradient(120deg,#1e1c22 0%,#3b2e36 55%,#7a5a5e 100%)}
.hero-tile-a{left:620px;top:388px;width:289px;height:219px;background:linear-gradient(135deg,#3a2620 0%,#7a5446 60%,#4a3028 100%)}
.hero-tile-b{left:911px;top:388px;width:289px;height:219px;background:linear-gradient(135deg,#8a6a52 0%,#c9a48a 55%,#5c4030 100%)}
.hero-title{left:100px;top:300px;color:var(--white);font-size:108px;line-height:112px}
.hero-title span{display:block;padding-left:58px}
.slider-arrows{left:548px;top:488px;display:flex;gap:2px}
.slider-arrows span{width:24px;height:23px;background:var(--orange);display:flex;align-items:center;justify-content:center}
.hero-sub{left:873px;top:245px;color:var(--white);font-size:58px}
.btn-book{left:965px;top:324px;width:136px;height:34px;border:2px solid var(--orange);color:var(--orange);font-size:13px;font-weight:700;text-align:center;line-height:30px;background:rgba(0,0,0,.3)}
.tile-title{color:var(--white);font-size:28px;white-space:nowrap}
.tile-note{color:var(--white);font-size:11px;font-weight:700}

/* bands */
.band{left:0;width:1200px;background:var(--orange)}
.welcome{top:607px;height:323px}
.section-title{left:0;width:1200px;text-align:center;font-size:36px}
.divider{left:546px;width:108px;height:12px}
.welcome-copy{left:140px;top:717px;width:920px;text-align:center;color:var(--white);font-size:12px;line-height:28px}
.btn{height:41px;font-size:14px;font-weight:700;text-align:center;line-height:37px;text-transform:uppercase}
.btn-read{left:443px;top:832px;width:152px;border:2px solid var(--white);color:var(--white)}
.btn-today{left:605px;top:832px;width:153px;border:2px solid var(--ink);color:var(--ink)}

/* services */
.service-lead{left:99px;top:1058px;width:548px;height:428px;background:var(--dark)}
.service-lead .photo{width:548px;height:273px;background:linear-gradient(180deg,#e4e2dc 0%,#cfcbc2 55%,#6f8a45 75%,#4f6a30 100%)}
.service-card{top:1058px;width:207px;height:428px;border:1px solid var(--rule);background:var(--white)}
.service-card .photo{width:205px;height:273px;background:linear-gradient(160deg,#f2efe9 0%,#d9cfc2 50%,#b9644a 100%)}
.card-title{width:100%;text-align:center;font-size:20px;margin-top:18px;white-space:nowrap}
.card-text{text-align:center;font-size:11px;line-height:21px;margin:6px auto 0}
.service-lead .card-title{color:var(--white)}
.service-lead .card-text{color:#dcd8d4;width:470px}
.service-card .card-title{color:var(--ink)}
.service-card .card-text{width:186px}
.btn-more{height:31px;font-size:11px;line-height:27px;text-align:center;text-transform:uppercase;margin:14px auto 0}
.service-lead .btn-more{width:99px;border:2px solid var(--white);color:var(--white)}
.service-card .btn-more{width:99px;border:2px solid var(--orange);color:var(--orange)}
.section-rule{left:99px;top:1534px;width:1002px;height:1px;background:var(--rule)}

/* testimonial */
.avatar{left:141px;top:1652px;width:134px;height:134px;border-radius:50%;border:5px solid #e8e6e4;background:linear-gradient(160deg,#3a2a24 0%,#7a5038 60%,#b88050 100%)}
.author{left:343px;top:1654px;font-size:18px;color:var(--ink)}
.quote{left:343px;top:1699px;width:718px;font-size:12px;font-style:italic;line-height:30px;text-indent:34px}
.quote-mark{font-family:Georgia,serif;font-size:44px;color:#cfcac6;font-weight:700;line-height:1}

/* contact */
.contact{top:1838px;height:360px}
.field{border:2px solid var(--white);color:var(--white);font-size:12px;padding:6px 12px;text-transform:uppercase}
.btn-subscribe{left:142px;top:2111px;width:141px;height:39px;border:2px solid var(--ink);color:var(--ink);font-size:12px;font-weight:600;text-align:center;line-height:35px}
.info-head{left:789px;top:1962px;color:var(--white);font-size:17px}
.info-row{left:789px;color:var(--white);font-size:11px;line-height:22px;display:flex;gap:12px;text-transform:uppercase}
.info-row svg{flex:none;margin-top:4px}

/* footer */
.social{top:2219px;width:28px;height:28px;border-radius:50%;background:var(--orange)}
.footer-links{left:0;top:2258px;width:1200px;text-align:center;font-size:11px;color:var(--ink);word-spacing:2px}
.copyright{left:0;top:2279px;width:1200px;text-align:center;font-size:10px;color:var(--ink)}
</style>
</head>
<body>

<header class="abs site-nav">
  <div class="abs nav-active"></div>
  <a class="abs nav-link script is-active" style="left:147px">Home</a>
  <a class="abs nav-link script" style="left:278px">About me</a>
  <a class="abs nav-link script" style="left:409px">Services</a>
  <a class="abs nav-link script" style="left:795px">Gallery</a>
  <a class="abs nav-link script" style="left:931px">Book me</a>
  <a class="abs nav-link script" style="left:1070px">Contact us</a>
</header>
<div class="abs brand-plate"></div>
<div class="abs brand-name script">Velvet Veil</div>

<section>
  <div class="abs photo hero-main" role="img" aria-label="Bride-to-be in a floral dress seated on vintage suitcases against a teal wooden wall"></div>
  <div class="abs photo hero-top" role="img" aria-label="Model with a floral headpiece posing against a dark backdrop"></div>
  <div class="abs photo hero-tile-a" role="img" aria-label="Makeup artist applying eyeliner to a bride"></div>
  <div class="abs photo hero-tile-b" role="img" aria-label="Blonde bride having her makeup finished"></div>

  <h1 class="abs hero-title script">Bridal<span>Beauty</span></h1>
  <div class="abs slider-arrows">
    <span><svg width="8" height="10" viewBox="0 0 8 10"><path d="M6 1 2 5l4 4" stroke="#fff" stroke-width="1.6" fill="none"/></svg></span>
    <span><svg width="8" height="10" viewBox="0 0 8 10"><path d="M2 1l4 4-4 4" stroke="#fff" stroke-width="1.6" fill="none"/></svg></span>
  </div>
  <h2 class="abs hero-sub script">Individual</h2>
  <a class="abs btn-book">CLICK TO BOOK</a>

  <div class="abs" style="left:636px;top:534px">
    <div class="tile-title script">Totam rem Aperiam,</div>
    <div class="tile-note">LOREM IPSUM IS SIMPLY DUMMY...</div>
  </div>
  <div class="abs" style="left:928px;top:534px;width:260px;overflow:hidden">
    <div class="tile-title script">Totam rem Ape</div>
    <div class="tile-note">LOREM IPSUM IS SIMPLY DUMMY...</div>
  </div>
</section>

<section class="abs band welcome"></section>
<h2 class="abs section-title script" style="top:645px;color:var(--white)">Welcome to Velvet Veil</h2>
<svg class="abs divider" style="top:691px" viewBox="0 0 108 12"><line x1="0" y1="6" x2="46" y2="6" stroke="#fff"/><line x1="62" y1="6" x2="108" y2="6" stroke="#fff"/><circle cx="54" cy="6" r="4.5" fill="none" stroke="#fff"/><circle cx="54" cy="6" r="2" fill="#fff"/></svg>
<p class="abs welcome-copy">A professional stylist for over five years, Mara Ellison possess a great deal of passion for the world of beauty and believes that hair is a women's most prized ornament. As a hair artist, ninety percent of her direction with a hairstyle comes from the hair and the other ten percent from the client's request.<br>Ellison attributes her diverse technique and styling ability to her Lumen education and rich culture.</p>
<a class="abs btn btn-read">Click Read More</a>
<a class="abs btn btn-today">Book Now Today</a>

<section>
  <h2 class="abs section-title script" style="top:960px;color:var(--orange)">What we do?</h2>
  <svg class="abs divider" style="top:1009px" viewBox="0 0 108 12"><line x1="0" y1="6" x2="46" y2="6" stroke="#e98b2a"/><line x1="62" y1="6" x2="108" y2="6" stroke="#e98b2a"/><circle cx="54" cy="6" r="4.5" fill="none" stroke="#e98b2a"/><circle cx="54" cy="6" r="2" fill="#e98b2a"/></svg>

  <article class="abs service-lead">
    <div class="photo" role="img" aria-label="Red-haired bride in a white gown standing by a weathered barn wall"></div>
    <h3 class="card-title script">Sed ut perspiciatis unde omnis iste natu</h3>
    <p class="card-text">Nemo enim ipsam voluptatem quia voluptas sit aspernatur aut odit aut fugit, sed quia consequuntur magni dolores eos qui ratione voluptatem sequ...</p>
    <div class="btn-more">View More</div>
  </article>
  <article class="abs service-card" style="left:667px">
    <div class="photo" role="img" aria-label="Bride with red curls leaning on a wooden fence holding a bouquet"></div>
    <h3 class="card-title script">Sed ut perspiciatis unde</h3>
    <p class="card-text">Nemo enim ipsam voluptatemed<br>quia voluptas sit asper.....</p>
    <div class="btn-more">View More</div>
  </article>
  <article class="abs service-card" style="left:894px">
    <div class="photo" role="img" aria-label="Smiling bride with side-swept red curls and a bouquet"></div>
    <h3 class="card-title script">Sed ut perspiciatis unde</h3>
    <p class="card-text">Nemo enim ipsam voluptatemed<br>quia voluptas sit asper.....</p>
    <div class="btn-more">View More</div>
  </article>
</section>
<div class="abs section-rule"></div>

<section>
  <h2 class="abs section-title script" style="top:1567px;color:var(--orange)">Testimonial</h2>
  <svg class="abs divider" style="top:1616px" viewBox="0 0 108 12"><line x1="0" y1="6" x2="46" y2="6" stroke="#e98b2a"/><line x1="62" y1="6" x2="108" y2="6" stroke="#e98b2a"/><circle cx="54" cy="6" r="4.5" fill="none" stroke="#e98b2a"/><circle cx="54" cy="6" r="2" fill="#e98b2a"/></svg>
  <svg class="abs" style="left:97px;top:1735px" width="12" height="30" viewBox="0 0 12 30"><path d="M10 1 2 15l8 14" stroke="#e3dfdb" stroke-width="2" fill="none"/></svg>
  <svg class="abs" style="left:1086px;top:1735px" width="12" height="30" viewBox="0 0 12 30"><path d="M2 1l8 14-8 14" stroke="#e3dfdb" stroke-width="2" fill="none"/></svg>
  <div class="abs avatar" role="img" aria-label="Portrait of the stylist with long ombré curls"></div>
  <div class="abs author script">-Mara Ellison</div>
  <div class="abs quote-mark" style="left:343px;top:1695px">&ldquo;</div>
  <p class="abs quote">A professional stylist for over five years, Mara Ellison possess a great deal of passion for the world of beauty and believes that hair is a women's most prized ornament. As a hair artist, ninety percent of her direction with a hairstyle comes from the hair and the other ten percent from the client's request. Ellison attributes her diverse technique and styling ability to her...</p>
  <div class="abs quote-mark" style="left:950px;top:1767px">&rdquo;</div>
</section>

<section class="abs band contact"></section>
<h2 class="abs section-title script" style="top:1872px;color:var(--white)">Contact Information</h2>
<svg class="abs divider" style="top:1918px" viewBox="0 0 108 12"><line x1="0" y1="6" x2="46" y2="6" stroke="#fff"/><line x1="62" y1="6" x2="108" y2="6" stroke="#fff"/><circle cx="54" cy="6" r="4.5" fill="none" stroke="#fff"/><circle cx="54" cy="6" r="2" fill="#fff"/></svg>
<form>
  <div class="abs field" style="left:142px;top:1969px;width:289px;height:34px">Name</div>
  <div class="abs field" style="left:440px;top:1969px;width:287px;height:34px">Email</div>
  <div class="abs field" style="left:142px;top:2012px;width:585px;height:87px">Subject</div>
  <div class="abs btn-subscribe">SUBSCRIE NOW</div>
</form>
<div class="abs info-head">VELVET VEIL</div>
<div class="abs info-row" style="top:2005px">
  <svg width="14" height="18" viewBox="0 0 14 18"><path d="M7 0a7 7 0 0 0-7 7c0 5 7 11 7 11s7-6 7-11a7 7 0 0 0-7-7z" fill="#fff"/><circle cx="7" cy="7" r="2.6" fill="#e98b2a"/></svg>
  <span>123 , Company name lorem ipsum dummy<br>street name,City name-47645</span>
</div>
<div class="abs info-row" style="top:2058px">
  <svg width="14" height="14" viewBox="0 0 14 14"><path d="M3 0l3 3-1.8 2a8 8 0 0 0 4.8 4.8L11 8l3 3-2 2.5C6 13 1 8 .5 2z" fill="#fff"/></svg>
  <span>Phone: +111 -000-0000</span>
</div>
<div class="abs info-row" style="top:2092px">
  <svg width="14" height="11" viewBox="0 0 14 11"><rect width="14" height="11" fill="#fff"/><path d="M0 0l7 6 7-6" stroke="#e98b2a" stroke-width="1.2" fill="none"/></svg>
  <span style="text-transform:none">Email: info@velvetveil.com.au</span>
</div>

<footer>
  <span class="abs social" style="left:511px"></span>
  <span class="abs social" style="left:548px"></span>
  <span class="abs social" style="left:586px"></span>
  <span class="abs social" style="left:622px"></span>
  <span class="abs social" style="left:659px"></span>
  <nav class="abs footer-links">HOME &nbsp;| &nbsp;ABOUT ME &nbsp;| &nbsp;SERVICES &nbsp;| &nbsp;GALLERY &nbsp;| &nbsp;BOOK ME &nbsp;| &nbsp;CONTACT US</nav>
  <p class="abs copyright">COPYRIGHTS©VELVET VEIL,2016 | ALLRIGHTS RESERVED.</p>
</footer>

</body>
</html>
```